Web Design Project

Psychotherapy and Counselling Practice needs a landing page web design.

My business "Larkspur Advisory" specialises in the treatment of Anxiety and Depression with a holistic approach, endeavouring to unlock the key that holds us to ransom in a life that is imbalanced, frustrating, and ultimately of our own making due to our own perceptions and behaviours.

There is much that impacts us which we cannot change, but we are always in control of how we think, and how we frame our experiences.....learning to challenge those thoughts and behaviours that are destructive and disempowering opens up a world of joyful possibility. Life is about making choices, learn to make wiser and healthier choices.......

Larkspur Advisory has a client base of individual clients but will seek to expand to offer services to the Corporate world by offering an adjunct to employers for established "Wellness Programs".

Larkspur Advisory is a highly professional, ethically bound business, with the needs of the client at the forefront of all we do.

Larkspur Advisory wishes to avoid the usual "jargon driven" psychobabble offered on many counselling web pages. It aims to be stylishly presented, clean in look and with as few "words" as possible and a largely white background (faster loading and more powerful impact of what is stated), those words contained in the webpage should be meaningful, persuasive and have an impact simply at glance. Larkspur does not want , or expect, those prospective clients in need of support , to be reading through volumes of industry driven cliches.

At this point Larkspur is just looking for a high quality landing page. However in time this will likely expand to include other sections such as case studies, video content etc.

Target Market(s)

Those in need of emotional support, suffering mental health issues, and those simply wanting to become self aware supported by a mindful therapist.

Industry/Entity Type

Industry

Requirements
Must have
• The design must incorporate the Larkspur logo and colour schemes found on the attached files.

```html
<!DOCTYPE html>
<html lang="en">
<head>
<meta charset="utf-8">
<title>Larkspur Advisory</title>
<link rel="stylesheet" href="https://fonts.googleapis.com/css2?family=Open+Sans:wght@400;600;700&family=Raleway:wght@300;400&display=swap">
<style>
:root{
  --green:#80ad1a;
  --green-dark:#6f9a12;
  --band:#6d6d6d;
  --map:#7c7c7c;
  --ink:#3c3c3c;
  --muted:#555;
  --white:#fff;
  --video:#2f2f2f;
  --rule:#d8d8d8;
}
*{margin:0;padding:0;box-sizing:border-box}
html,body{width:1200px;height:1089px;overflow:hidden;background:var(--white)}
body{position:relative;font-family:"Open Sans",Arial,sans-serif;color:var(--ink)}
.abs{position:absolute}
.brand{font-family:"Raleway",Arial,sans-serif;font-weight:300;color:var(--green);white-space:nowrap}
.brand-main{left:215px;top:110px;font-size:54px}
.account{left:560px;top:26px;font-size:11px;font-weight:600;color:#222}
.phone{left:847px;top:20px;font-size:23px;color:#555;font-family:"Raleway",Arial,sans-serif}
.phone b{color:var(--green);font-weight:700;margin-right:10px}
.main-nav{left:519px;top:68px;width:510px;height:47px;background:var(--green);display:flex;align-items:center;justify-content:center}
.main-nav a{color:var(--white);text-decoration:none;font-weight:700;font-size:19px;padding:0 13px;border-left:1px solid rgba(255,255,255,.5);line-height:14px}
.main-nav a:first-child{border-left:0}
.tagline{left:540px;top:122px;width:480px}
.tagline h1{font-family:"Raleway",Arial,sans-serif;font-weight:400;color:var(--green);font-size:39px;line-height:46px;white-space:nowrap}
.tagline p{font-size:23px;line-height:29px;color:#444;padding-left:20px;white-space:nowrap}
.search{left:805px;top:242px;width:199px;height:21px;border:2px solid #aaa;border-radius:11px;background:#f4f4f4;font-size:11px;color:#555;padding:2px 8px}
.search svg{position:absolute;right:6px;top:2px}
.social{display:flex;gap:4px}
.social span{width:27px;height:27px;border-radius:50%;background:#111;display:block}
.social-top{left:887px;top:272px}
.band{left:0;top:281px;width:1200px;height:283px;background:var(--band)}
.world-map{left:185px;top:300px;width:860px;height:320px;background:radial-gradient(ellipse at center,var(--map) 0%,rgba(124,124,124,0) 70%)}
.mission{left:150px;top:342px;width:900px;text-align:center;color:var(--white);font-size:25px;line-height:34px}
.video{left:201px;top:471px;width:388px;height:260px;background:#111;padding:6px}
.video-inner{width:100%;height:100%;background:var(--video);position:relative}
.video-name{position:absolute;left:0;right:0;top:140px;text-align:center;font-family:"Raleway",Arial,sans-serif;font-weight:300;font-size:50px;color:#4a4a4a}
.play{position:absolute;left:143px;top:93px;width:88px;height:58px;background:rgba(0,0,0,.45);border-radius:6px}
.cta{left:667px;top:526px;width:296px;height:54px;background:var(--green);color:var(--white);font-weight:600;font-size:28px;display:flex;align-items:center;justify-content:center}
.statement{left:612px;top:644px;width:410px;text-align:right;font-size:20px;line-height:31px;color:var(--muted);white-space:nowrap}
.statement em{font-style:normal;color:var(--green)}
.features{left:172px;top:770px;width:858px;display:flex}
.feature{width:286px;height:190px;text-align:center;position:relative;padding:0 14px}
.feature + .feature{border-left:1px dotted var(--rule)}
.feature + .feature::before{content:"";position:absolute;left:-3px;top:4px;width:4px;height:26px;background:var(--green)}
.feature h2{font-weight:400;font-size:24px;color:var(--green);line-height:30px;margin-bottom:8px}
.feature p{font-size:12.5px;line-height:20.5px;color:#444;height:92px}
.feature a{display:inline-block;margin-top:10px;background:var(--green);color:var(--white);text-decoration:none;font-weight:600;font-size:14px;width:145px;height:33px;line-height:33px}
.footer-shadow{left:170px;top:956px;width:860px;height:12px;background:radial-gradient(ellipse at center top,rgba(0,0,0,.12),rgba(0,0,0,0) 70%)}
.footer-nav{left:196px;top:1002px;font-size:14px;font-weight:600;color:#444}
.footer-nav a{color:#444;text-decoration:none;padding:0 7px;border-left:2px solid #666}
.footer-nav a:first-child{padding-left:0;border-left:0}
.copyright{left:196px;top:1030px;font-size:12px;color:#555}
.social-foot{left:716px;top:1020px}
.brand-foot{left:866px;top:1016px;font-size:28px}
</style>
</head>
<body>
  <div class="abs brand brand-main">LARKSPUR</div>

  <div class="abs account">Login &nbsp;|&nbsp; Register</div>
  <div class="abs phone"><b>M</b>0400 123 987</div>

  <nav class="abs main-nav">
    <a href="#">HOME</a><a href="#">ABOUT</a><a href="#">SERVICES</a><a href="#">CONTACT</a><a href="#">FAQS</a>
  </nav>

  <div class="abs tagline">
    <h1>Your wellness starts today</h1>
    <p>specialises in the treatment of Anxiety and<br>Depression with a holistic approach</p>
  </div>

  <div class="abs band"></div>
  <div class="abs world-map" role="img" aria-label="Dotted world map behind the mission statement"></div>

  <svg class="abs" style="left:0;top:240px" width="1200" height="380" viewBox="0 0 1200 380" aria-hidden="true">
    <path d="M0 0 H1200 V41 H0 Z" fill="#fff"/>
    <path d="M172 20 Q 170 45 210 44 C 420 28 640 22 790 20 C 650 30 420 40 230 48 Q 172 52 172 20 Z" fill="var(--green)"/>
    <path d="M172 38 C 300 52 500 44 790 20 L 790 41 L172 41 Z" fill="#fff"/>
    <path d="M589 345 C 700 395 900 385 1030 325 L1030 324 L1200 324 L1200 380 L589 380 Z" fill="#fff"/>
    <path d="M589 340 C 700 388 900 378 1030 318 C 900 370 720 380 589 352 Z" fill="var(--green)"/>
  </svg>

  <div class="abs search">Search
    <svg width="14" height="14" viewBox="0 0 14 14"><circle cx="5.5" cy="5.5" r="4" fill="none" stroke="#555" stroke-width="1.8"/><path d="M8.5 8.5 L13 13" stroke="#555" stroke-width="2"/></svg>
  </div>
  <div class="abs social social-top"><span></span><span></span><span></span><span></span></div>

  <p class="abs mission">DANA REID commitment to provide quality healthcare for your<br>whole family drives everything we do.</p>

  <div class="abs video">
    <div class="video-inner">
      <div class="video-name">LARKSPUR</div>
      <div class="play"><svg width="88" height="58" viewBox="0 0 88 58"><path d="M34 15 L58 29 L34 43 Z" fill="#ddd"/></svg></div>
    </div>
  </div>

  <div class="abs cta">Consult Us Today!</div>

  <p class="abs statement"><em>Larkspur Advisory is a highly professional,<br>ethically bound business,</em> with the needs of<br>the client at the forefront of all we do.</p>

  <section class="abs features">
    <div class="feature">
      <h2>Who We Are</h2>
      <p>Lorem ipsum dolor sit amet, consectetuer adipiscing elit, sed diam nonummy nibh euismod tincidunt ut laoreet dolore magna aliquam erat volutpat.</p>
      <a href="#">GET TO KNOW US</a>
    </div>
    <div class="feature">
      <h2>We’re Growing!</h2>
      <p>Ut wisi enim ad minim veniam, quis nostrud exerci tation ullamcorper suscipit lobortis nisl ut aliquip ex ea commodo consequat.</p>
      <a href="#">HOW WE HELPS</a>
    </div>
    <div class="feature">
      <h2>Let’s Talk about You</h2>
      <p>Duis autem vel eum iriure dolor in hendrerit in vulputate velit esse molestie consequat, vel illum dolore eu feugiat nulla facilisis at vero eros et accumsan et iusto odio.</p>
      <a href="#">CONSULT US</a>
    </div>
  </section>

  <div class="abs footer-shadow"></div>
  <nav class="abs footer-nav"><a href="#">HOME</a><a href="#">ABOUT</a><a href="#">SERVICES</a><a href="#">CONTACT</a><a href="#">FAQS</a></nav>
  <p class="abs copyright">Copyright © 2013 Larkspur</p>
  <div class="abs social social-foot"><span></span><span></span><span></span><span></span></div>
  <div class="abs brand brand-foot">LARKSPUR</div>
</body>
</html>
```